Jewelry store needs fully functional Ecommerce website

Web Design Brief for our E-commerce Jewelry retail store.
Description

We need a fully coded Vendora website. The Vendora site will need to be fully functional with an Ecommerce integration (fully integrated with Coinlet and All other gateways) and will need to be SEO optimized.
We sell jewelry items like: rings, earrings, necklaces etc. The website should have an elegant, modern, professional, fun, look.

***We would like the website to look and function similarly to this website:
https://velvetrune.com

Color Preference
Colors to be used are white background with black font and light pink/ purple/ gold tints. We have attached our logo as reference.

Functionalities
The store will function like a typical Ecommerce jewelry store, using the products/categories as the starting page. Going into individual product pages by selecting images and leading to a detailed “buy now” page for the selected product.

Target Market
Jewelry lovers.

Should Not Have:
- - Dull and common design
- - Messy/unstructured navigation

Coded - Design and coding required
Target Audience are women from 16-50 years old.
We will need to be able to add products and make modifications to the website as needed.

We need the following apps installed and Operating:
-Shelf Tally; Parcel Finder (rename “track your order”) ; Query Desk (Questions and Answers) ; Vimt Reviews; Textazo; Brundel Email Marketing ; Tavolo (Chatterloop messenger bump) ; Brisk multi- currency (translate currency to buyer) ; Pricewise Extra ; Swift Reach form App
We will need all products imported: (below is information for importing products). We will provide all links that serve entire active item product catalog in vendoras import format:
DataFeed:

If you are getting started with Vendora, a combination of the Vendora Import Format and XML feeds is ideal. The Vendora Import Format will output a file that can be uploaded into Vendora’s product database. After you import, you can use the XML feed and a third party app to keep the inventory up to date in real time, take down items that go out of stock etc., all without regular human intervention. There a several Vendora apps that can do this type of feed integration. We have had a good experience with Shelf Tally, which is an app that can be configured to accept our XML feed and update products on a set schedule. You can even set your own margins based on our wholesale price with this app.

Vendora Formatted HTML TableTo make it easier to get started on Vendora, we included a format that outputs the required fields for a product import in Vendora. In order to use the embedded Excel file, first open the file (Auto-Vendora-Datasheet-Format.xslx), Refresh it (under Data tab), and then Save As with a new file name in a CSV (UTF-8) file. That file can then be split into smaller CSV files (if there is a limit on the number of products per file) for import into Vendora.

Target Market(s)

Jewelry Lovers

Industry/Entity Type

Jewelry Store

Coding

Number of Pages Required

5+ page

Colors
eda3c7
d3a5cc
ffffff

Requirements
Must have
• Color Preference
Colors to be used are white background with black font and light pink/ purple/ gold tints.

https://velvetrune.com
Should not have
• Should Not Have:

```html
<!DOCTYPE html>
<html lang="en">
<head>
<meta charset="utf-8">
<title>Lumen Sable — Jewelry</title>
<link rel="stylesheet" href="https://fonts.googleapis.com/css2?family=Work+Sans:wght@400;500;600;700;800&family=Noto+Sans:wght@400;500;600;700&display=swap">
<style>
:root{
  --ink:#1d1b1c;
  --body:#3a3739;
  --muted:#6d676a;
  --lilac:#c9a3d1;
  --lilac-strong:#c48fc6;
  --pink:#eda3c7;
  --blush:#f4eff0;
  --card:#f3eeef;
  --white:#ffffff;
  --footer:#2b2a2b;
  --footer-text:#d9d4d6;
  --rule:#cfb9d6;
}
*{box-sizing:border-box;margin:0;padding:0}
html,body{width:1200px;height:4222px;overflow:hidden;background:var(--white)}
body{position:relative;font-family:"Noto Sans",sans-serif;color:var(--body)}
.abs{position:absolute}
.btn{position:absolute;display:flex;align-items:center;justify-content:center;background:var(--lilac);color:var(--white);font-family:"Work Sans",sans-serif;font-weight:600;letter-spacing:.04em;text-transform:uppercase}
.section-title{position:absolute;left:0;width:1200px;text-align:center;font-family:"Work Sans",sans-serif;font-weight:600;font-size:24px;color:var(--ink);letter-spacing:.02em}
.section-title::after{content:"";display:block;width:46px;height:2px;background:var(--rule);margin:14px auto 0}
.photo{position:absolute}

/* header */
.site-header{position:absolute;left:0;top:0;width:1200px;height:108px}
.brand{position:absolute;display:flex;align-items:center;gap:12px}
.brand-dot{border-radius:50%;background:var(--lilac)}
.brand-name{font-family:"Work Sans",sans-serif;font-weight:500;color:var(--lilac-strong)}
.promo{position:absolute;left:600px;top:28px;font-size:12px;color:var(--ink);font-weight:500}
.nav{position:absolute;left:598px;top:72px;display:flex;gap:0;font-family:"Work Sans",sans-serif;font-size:14px;color:var(--ink);font-weight:500}
.nav a{color:inherit;text-decoration:none;margin-right:44px}
.nav a:last-child{margin-right:0}
.nav a.active{color:var(--lilac);border-bottom:1px solid var(--lilac)}
.header-icons{position:absolute;left:890px;top:22px;display:flex;gap:20px;align-items:center}
.cart-badge{position:absolute;left:1050px;top:16px;width:18px;height:18px;border-radius:50%;background:var(--lilac);color:#fff;font-size:10px;display:flex;align-items:center;justify-content:center}

/* hero */
.hero{position:absolute;left:0;top:108px;width:1200px;height:590px;background:linear-gradient(90deg,#3a322d 0%,#5e554b 35%,#7a6f62 55%,#4c4239 100%)}
.hero h1{position:absolute;left:130px;top:150px;font-family:"Work Sans",sans-serif;font-weight:800;font-size:50px;color:#fff;letter-spacing:.03em}
.hero p{position:absolute;left:133px;top:230px;width:420px;font-size:20px;line-height:33px;color:#f1ecea}
.hero .btn{left:133px;top:326px;width:149px;height:41px;font-size:17px;color:var(--ink)}
.hero-dots{position:absolute;left:562px;top:550px;display:flex;gap:10px}
.hero-dots span{width:7px;height:7px;border-radius:50%;background:#fff}
.hero-dots span.on{background:#7bbf4a}

/* categories */
.category{position:absolute;top:724px;height:315px}
.category h3{position:absolute;font-family:"Work Sans",sans-serif;font-weight:600;font-size:18px;color:var(--ink)}
.category p{position:absolute;font-size:12.5px;line-height:18px;width:160px}
.category .btn{width:105px;height:31px;font-size:13px}

/* products */
.product{position:absolute;top:1160px;height:384px;background:var(--card)}
.product .photo{left:50%;transform:translateX(-50%);top:24px;width:190px;height:190px}
.product h4,.seller h4{position:absolute;left:0;width:100%;text-align:center;font-family:"Work Sans",sans-serif;font-weight:600;font-size:15px;color:var(--ink)}
.product .price,.seller .price{position:absolute;left:0;width:100%;text-align:center;font-size:19px;color:var(--ink)}
.product .btn,.seller .btn{left:50%;transform:translateX(-50%);width:98px;height:26px;font-size:11px}

/* welcome */
.welcome-kicker{position:absolute;left:693px;top:1622px;font-family:"Work Sans",sans-serif;font-size:21px;color:var(--ink);font-weight:500}
.welcome-title{position:absolute;left:693px;top:1646px;font-family:"Work Sans",sans-serif;font-weight:700;font-size:36px;color:var(--ink)}
.welcome-title::after{content:"";display:block;width:176px;height:2px;background:var(--rule);margin-top:6px}
.copy{position:absolute;font-size:14.5px;line-height:22.5px;color:var(--body)}

/* best sellers */
.band{position:absolute;left:0;width:1200px;background:var(--blush)}
.seller{position:absolute;top:2165px;width:370px;height:510px}
.seller .photo{left:0;top:0;width:370px;height:384px}

/* why */
.why-title{position:absolute;left:131px;top:2790px;font-family:"Work Sans",sans-serif;font-weight:700;font-size:31px;color:var(--ink);letter-spacing:.02em}
.why-title::after{content:"";display:block;width:64px;height:3px;background:var(--lilac);margin-top:14px}

/* testimonials */
.testimonial{position:absolute;top:3321px;height:291px;background:#fff}
.testimonial .quote{position:absolute;left:22px;top:18px;font-family:"Work Sans",sans-serif;font-weight:700;font-size:30px;color:var(--ink);line-height:1}
.testimonial p{position:absolute;left:38px;top:50px;width:228px;font-size:12px;line-height:18.5px;color:var(--body)}
.author{position:absolute;left:38px;top:230px;display:flex;align-items:center;gap:10px}
.avatar{width:32px;height:32px;border-radius:50%;background:linear-gradient(135deg,#b9a79a,#6f6258)}
.author b{display:block;font-size:12px;color:var(--ink);font-weight:700}
.author span{font-size:11px;color:var(--muted)}

/* newsletter */
.newsletter{position:absolute;left:0;top:3660px;width:1200px;height:220px;background:var(--lilac-strong)}
.newsletter h2{position:absolute;left:0;top:48px;width:1200px;text-align:center;font-family:"Work Sans",sans-serif;font-weight:600;font-size:24px;color:#fff;letter-spacing:.02em}
.newsletter .sub{position:absolute;left:0;top:80px;width:1200px;text-align:center;font-size:16px;color:#f6e8f4}
.subscribe{position:absolute;left:323px;top:128px;width:554px;height:51px;background:#fff;border:2px solid #e7d6e6}
.subscribe label{position:absolute;left:20px;top:15px;font-size:12px;color:var(--ink)}
.subscribe .btn{left:417px;top:4px;width:128px;height:39px;background:var(--pink);font-size:16px;letter-spacing:.03em}

/* footer */
.site-footer{position:absolute;left:0;top:3880px;width:1200px;height:342px;background:var(--footer);color:var(--footer-text)}
.footer-col{position:absolute;top:52px;font-size:12px}
.footer-col h5{font-family:"Work Sans",sans-serif;font-weight:700;font-size:13px;color:#fff;letter-spacing:.03em;margin-bottom:22px}
.footer-col li{list-style:none;line-height:20px}
.contact-item,.social-item{display:flex;align-items:flex-start;gap:12px;margin-bottom:22px;line-height:16px}
.circle{flex:none;width:22px;height:22px;border-radius:50%;background:#fff;display:flex;align-items:center;justify-content:center}
.footer-rule{position:absolute;left:131px;top:268px;width:936px;height:1px;background:#4a474a}
.copyright{position:absolute;left:0;top:302px;width:1200px;text-align:center;font-size:10px;color:#b9b4b6}
</style>
</head>
<body>

<header class="site-header">
  <div class="brand" style="left:131px;top:30px">
    <span class="brand-dot" style="width:40px;height:40px"></span>
    <span class="brand-name" style="font-size:28px">Lumen Sable</span>
  </div>
  <div class="promo">FREE US SHIPPING ON ORDERS $50+</div>
  <nav class="nav">
    <a class="active">HOME</a><a>ABOUT US</a><a>SERVICES</a><a>SHOP</a><a>CONTACT US</a>
  </nav>
  <div class="header-icons">
    <svg width="26" height="26" viewBox="0 0 26 26" aria-label="Account"><circle cx="13" cy="13" r="11" fill="none" stroke="#1d1b1c" stroke-width="2"/><circle cx="13" cy="10" r="4" fill="#1d1b1c"/><path d="M6 20c2-4 12-4 14 0" fill="#1d1b1c"/></svg>
    <svg width="26" height="24" viewBox="0 0 26 24" aria-label="Wishlist"><path d="M13 21S3 14 3 8a5 5 0 0 1 10-1 5 5 0 0 1 10 1c0 6-10 13-10 13z" fill="none" stroke="#1d1b1c" stroke-width="1.8"/></svg>
    <svg width="24" height="24" viewBox="0 0 24 24" aria-label="Search"><circle cx="10" cy="10" r="7" fill="none" stroke="#1d1b1c" stroke-width="2.6"/><path d="M15 15l7 7" stroke="#1d1b1c" stroke-width="3"/></svg>
    <svg width="32" height="30" viewBox="0 0 32 30" aria-label="Cart"><path d="M2 4h5l4 16h16l3-12H9" fill="none" stroke="#1d1b1c" stroke-width="2"/><circle cx="13" cy="25" r="2.4" fill="#1d1b1c"/><circle cx="25" cy="25" r="2.4" fill="#1d1b1c"/></svg>
  </div>
  <span class="cart-badge">0</span>
</header>

<section class="hero" role="img" aria-label="Woman wearing gold earrings, necklace, ring and bracelet">
  <h1>JEWELRY</h1>
  <p>Lorem Ipsum is simply dummy text of the printing and typesetting industry.</p>
  <a class="btn">READ MORE</a>
  <div class="hero-dots"><span></span><span></span><span class="on"></span><span></span><span></span></div>
</section>

<article class="category" style="left:133px;width:457px;background:linear-gradient(90deg,#c9a7a0 0%,#e4e6df 45%,#eef3e3 100%)" role="img" aria-label="Woman wearing drop earrings">
  <h3 style="left:258px;top:82px">FOR WOMEN</h3>
  <p style="left:259px;top:122px">Lorem Ipsum is simply dummy text of the printing and typesetting industry.</p>
  <a class="btn" style="left:259px;top:198px">SHOP NOW</a>
</article>
<article class="category" style="left:611px;width:456px;background:linear-gradient(90deg,#262426 0%,#3a383b 55%,#6e6b6f 100%)" role="img" aria-label="Man in black shirt wearing gold chain">
  <h3 style="left:273px;top:146px;color:#fff">FOR MEN</h3>
  <p style="left:274px;top:174px;color:#e6e2e4">Lorem Ipsum is simply dummy text of the printing and typesetting industry.</p>
  <a class="btn" style="left:274px;top:243px">SHOP NOW</a>
</article>

<h2 class="section-title" style="top:1084px">OUR PRODUCTS</h2>

<article class="product" style="left:131px;width:298px">
  <div class="photo" role="img" aria-label="Diamond solitaire ring" style="background:radial-gradient(circle,#d9d9dc 0%,#b8b8bd 45%,var(--card) 72%)"></div>
  <h4 style="top:248px">LOREM IPSUM</h4><div class="price" style="top:278px">$15.99</div><a class="btn" style="top:320px">ADD TO CART</a>
</article>
<article class="product" style="left:449px;width:300px">
  <div class="photo" role="img" aria-label="Rose gold woven ring" style="background:radial-gradient(circle,#e9b88a 0%,#d9995f 45%,var(--card) 72%)"></div>
  <h4 style="top:248px">LOREM IPSUM</h4><div class="price" style="top:278px">$15.99</div><a class="btn" style="top:320px">ADD TO CART</a>
</article>
<article class="product" style="left:769px;width:298px">
  <div class="photo" role="img" aria-label="Gold chain necklace" style="background:radial-gradient(circle,#f2dc7c 0%,#e2c445 40%,var(--card) 72%)"></div>
  <h4 style="top:248px">LOREM IPSUM</h4><div class="price" style="top:278px">$15.99</div><a class="btn" style="top:320px">ADD TO CART</a>
</article>

<div class="photo" role="img" aria-label="Gold rings and earrings arranged on a reflective surface" style="left:131px;top:1601px;width:513px;height:379px;background:linear-gradient(180deg,#9c8a78 0%,#b8a590 50%,#8a7866 100%)"></div>
<div class="welcome-kicker">WELCOME TO</div>
<h2 class="welcome-title">LUMEN SABLE</h2>
<p class="copy" style="left:693px;top:1729px;width:376px">There are many variations of passages of Lorem Ipsum available, but the majority have suffered alteration in some form, by injected humour, or randomised words which don't look even slightly believable. If you are going to use a passage of Lorem Ipsum, you need to be sure there isn't anything embarrassing hidden in the middle of text.</p>
<a class="btn" style="left:698px;top:1921px;width:103px;height:31px;font-size:13px">READ MORE</a>

<section class="band" style="top:2047px;height:672px"></section>
<h2 class="section-title" style="top:2087px">BEST SELLERS</h2>
<article class="seller" style="left:28px">
  <div class="photo" role="img" aria-label="Woman wearing layered gold necklaces" style="background:linear-gradient(135deg,#e9d2c6 0%,#c79a86 50%,#a97c68 100%)"></div>
  <h4 style="top:406px;left:-28px;width:330px">LOREM IPSUM</h4><div class="price" style="top:436px;left:-28px;width:330px">$15.99</div><a class="btn" style="top:479px;left:137px">ADD TO CART</a>
</article>
<article class="seller" style="left:418px">
  <div class="photo" role="img" aria-label="Stack of ornate gold bangles" style="background:linear-gradient(135deg,#5a3a1c 0%,#b98a36 50%,#6b4520 100%)"></div>
  <h4 style="top:406px">LOREM IPSUM</h4><div class="price" style="top:436px">$15.99</div><a class="btn" style="top:479px">ADD TO CART</a>
</article>
<article class="seller" style="left:805px">
  <div class="photo" role="img" aria-label="Woman wearing silver necklace and drop earrings" style="background:linear-gradient(135deg,#d6b2a1 0%,#c49a88 50%,#7b6660 100%)"></div>
  <h4 style="top:406px;left:20px;width:350px">LOREM IPSUM</h4><div class="price" style="top:436px;left:20px;width:350px">$15.99</div><a class="btn" style="top:479px;left:195px">ADD TO CART</a>
</article>

<h2 class="why-title">WHY CHOOSE US</h2>
<p class="copy" style="left:131px;top:2869px;width:340px">There are many variations of passages of Lorem Ipsum available, but the majority have suffered alteration in some form, by injected humour, or randomised words which don't look even slightly believable. If you are going to use a passage of Lorem Ipsum, you need to be sure there isn't anything embarrassing hidden.</p>
<a class="btn" style="left:131px;top:3073px;width:105px;height:31px;font-size:13px">READ MORE</a>
<div class="photo" role="img" aria-label="Woman in pink dress wearing a colourful pendant and ring" style="left:516px;top:2767px;width:551px;height:377px;background:linear-gradient(90deg,#efc6cb 0%,#e7b3ba 45%,#c89ccb 100%)"></div>

<section class="band" style="top:3193px;height:467px"></section>
<h2 class="section-title" style="top:3240px">TESTIMONIALS</h2>
<article class="testimonial" style="left:131px;width:298px">
  <span class="quote">“</span>
  <p>Lorem ipsum dolor sit amet, cons ectetur adipiscing elit, sed do eiusmod tempor incididunt ut labore et dolore magna aliqua. Ut enim ad minim veni am, quis nostrud exercitation ullamco laboris nisi ut aliquip ex ea commodo consequat. Duis aute irure dolor in reprehenderit in voluptate velit esse cillum dolore</p>
  <div class="author"><span class="avatar" role="img" aria-label="Reviewer portrait"></span><div><b>MARLOW</b><span>England</span></div></div>
</article>
<article class="testimonial" style="left:452px;width:300px">
  <span class="quote">“</span>
  <p>Lorem ipsum dolor sit amet, cons ectetur adipiscing elit, sed do eiusmod tempor incididunt ut labore et dolore magna aliqua. Ut enim ad minim veni am, quis nostrud exercitation ullamco laboris nisi ut aliquip ex ea commodo consequat. Duis aute irure dolor in reprehenderit in voluptate velit esse cillum dolore</p>
  <div class="author"><span class="avatar" role="img" aria-label="Reviewer portrait"></span><div><b>MARLOW</b><span>England</span></div></div>
</article>
<article class="testimonial" style="left:775px;width:300px">
  <span class="quote">“</span>
  <p>Lorem ipsum dolor sit amet, cons ectetur adipiscing elit, sed do eiusmod tempor incididunt ut labore et dolore magna aliqua. Ut enim ad minim veni am, quis nostrud exercitation ullamco laboris nisi ut aliquip ex ea commodo consequat. Duis aute irure dolor in reprehenderit in voluptate velit esse cillum dolore</p>
  <div class="author"><span class="avatar" role="img" aria-label="Reviewer portrait"></span><div><b>MARLOW</b><span>England</span></div></div>
</article>

<section class="newsletter">
  <h2>NEWSLETTER SUBSCRIBE</h2>
  <div class="sub">Lorem ipsum dolor sit amet cons ectetur adipiscing elit</div>
  <div class="subscribe"><label>E MAIL ID</label><a class="btn">SUBSCRIBE</a></div>
</section>

<footer class="site-footer">
  <div class="brand" style="left:131px;top:80px">
    <span class="brand-dot" style="width:54px;height:54px"></span>
    <span class="brand-name" style="font-size:32px">Lumen Sable</span>
  </div>
  <div class="footer-col" style="left:497px">
    <h5>MENU</h5>
    <ul><li>HOME</li><li>ABOUT US</li><li>SERVICES</li><li>SHOP</li><li>CONTACT US</li></ul>
  </div>
  <div class="footer-col" style="left:661px">
    <h5>CONTACT US</h5>
    <div class="contact-item"><span class="circle"><svg width="10" height="13" viewBox="0 0 10 13"><path d="M5 0a5 5 0 0 1 5 5c0 3-5 8-5 8S0 8 0 5a5 5 0 0 1 5-5z" fill="#2b2a2b"/><circle cx="5" cy="5" r="1.8" fill="#fff"/></svg></span><div>5120 Larkmoor Lane<br>Dunmere, CA 90000</div></div>
    <div class="contact-item"><span class="circle"><svg width="12" height="12" viewBox="0 0 12 12"><path d="M2 0l2.5 3-1.5 1.5a8 8 0 0 0 4.5 4.5L9 7.5 12 10l-2 2C5 12 0 7 0 2z" fill="#2b2a2b"/></svg></span><div>Call Us<br>555.010.2040</div></div>
    <div class="contact-item"><span class="circle"><svg width="12" height="9" viewBox="0 0 12 9"><rect width="12" height="9" rx="1" fill="#2b2a2b"/><path d="M0 1l6 4 6-4" fill="none" stroke="#fff" stroke-width="1"/></svg></span><div>E mail Us<br>info@lumensable.example</div></div>
  </div>
  <div class="footer-col" style="left:960px">
    <h5>FOLLOW US</h5>
    <div class="social-item"><span class="circle"></span><div>Like us on<br>CHATTERLOOP</div></div>
    <div class="social-item"><span class="circle"></span><div>Follow us on<br>CHIRPLINE</div></div>
    <div class="social-item"><span class="circle"></span><div>Follow us on<br>LINKWELL</div></div>
  </div>
  <div class="footer-rule"></div>
  <div class="copyright">Copyright © 2021 All Rights Reserved</div>
</footer>

</body>
</html>
```